Real Estate "For Sale" Sign for construction company

We need a sign that we can use to hang on a post and place on the road when we sell a property. The sign will be simple and will need to mainly feature our logo (files attached), as well as the words "For Sale", and then our phone number "(555) 617 3489". The sign will hang on a post that'll look something like the attached picture.

Target Market(s)

Home buyers

Industry/Entity Type

Real Estate

Font styles to use
Serif
Sans Serif

Colors
0054AA
0677BA
7BADD7
CADEEF
E8F1F8
0094D4
00A9DD
6FCCEA
C7EBF8
E9F6FB

Requirements
Must have
• For Sale & our phone number

```html
<!DOCTYPE html>
<html lang="en">
<head>
<meta charset="utf-8">
<title>For Sale Sign – Ridgeline Homestead Realty</title>
<link href="https://fonts.googleapis.com/css2?family=Arimo:wght@400;700&display=swap" rel="stylesheet">
<style>
  :root {
    --backdrop: #a9aaae;
    --sign: #ffffff;
    --ink: #333333;
    --brand-blue: #2f80c4;
    --brand-mark: #0677ba;
  }
  * { margin: 0; padding: 0; box-sizing: border-box; }
  html, body {
    width: 1062px;
    height: 1200px;
    overflow: hidden;
    background: var(--backdrop);
    font-family: "Arimo", Arial, sans-serif;
  }
  .sign {
    position: absolute;
    left: 243px;
    top: 222px;
    width: 576px;
    height: 757px;
    background: var(--sign);
    color: var(--ink);
  }
  .sign > * { position: absolute; line-height: 1; white-space: nowrap; }
  .agent-name { left: 60px; font-size: 66px; font-weight: 400; }
  .agent-first { top: 51px; }
  .agent-last { top: 119px; }
  .divider { left: 60px; top: 205px; width: 364px; height: 1px; background: var(--ink); }
  .headline { left: 55px; top: 223px; font-size: 95px; font-weight: 700; letter-spacing: -0.5px; }
  .call-prompt { left: 0; width: 100%; text-align: center; top: 370px; font-size: 23px; }
  .phone { left: 55px; top: 410px; font-size: 62px; }
  .website { left: 0; width: 100%; text-align: center; top: 515px; font-size: 20px; }
  .brand-mark { left: 260px; top: 588px; }
  .brand-name { left: 0; width: 100%; text-align: center; top: 666px; font-size: 42px; color: var(--brand-blue); }
  .brand-tagline { left: 0; width: 100%; text-align: center; top: 718px; font-size: 14px; letter-spacing: 13px; padding-left: 13px; color: var(--brand-blue); }
</style>
</head>
<body>
  <div class="sign">
    <div class="agent-name agent-first">Jane</div>
    <div class="agent-name agent-last">Last Name</div>
    <div class="divider"></div>
    <div class="headline">For Sale</div>
    <div class="call-prompt">CALL OR TEXT ME AT</div>
    <div class="phone">(555) 617 3489</div>
    <div class="website">yourwebsitegoeshere.com</div>
    <svg class="brand-mark" width="56" height="56" viewBox="0 0 56 56" aria-hidden="true">
      <circle cx="28" cy="28" r="28" fill="var(--brand-mark)"/>
    </svg>
    <div class="brand-name">Ridgeline Homestead</div>
    <div class="brand-tagline">REALTY</div>
  </div>
</body>
</html>
```